Steady Meadowcap HEMP Cannabis CBD tinctures

We need packaging for our line of CBD product label design based in Oakland Ca Brand is called 'Steady Meadowcap'. Our initial product is tincture to help people with pain with out the High effect of THC. I will be attaching og other company sample. The design should communicate slick look and relay health. Use the logo as way to color

Target Market(s)

CBD

Font styles to use
Serif
Decorative

Requirements
Must have
• Design that will make it stand out from the rest of the product on the shelve and be bright.
Nice to have
• The package must be able to stand out and not be dominated by Black color the green color must be the main color.
Should not have
• Be all black and get lost on the shelves

```html
<!DOCTYPE html>
<html lang="en">
<head>
<meta charset="utf-8">
<title>Steady Meadowcap Hemp CBD Oil Packaging</title>
<link rel="stylesheet" href="https://fonts.googleapis.com/css2?family=Nunito:wght@400;700;800;900&family=Questrial&display=swap">
<style>
  :root {
    --canvas: #eef0ec;
    --green-deep: #1b5e24;
    --green-dark: #216e2a;
    --green-mid: #2e8b30;
    --lime: #8fcf3e;
    --lime-bright: #b6e357;
    --lime-pale: #d3f07c;
    --yellow-green: #cfe96a;
    --white: #ffffff;
    --ink: #1a1a1a;
  }
  * { box-sizing: border-box; margin: 0; padding: 0; }
  html, body { width: 1200px; height: 1050px; overflow: hidden; }
  body {
    background: var(--canvas);
    font-family: "Nunito", sans-serif;
    position: relative;
  }

  /* ---------- Label sheet ---------- */
  .label {
    position: absolute;
    top: 330px;
    width: 215px;
    height: 400px;
    border-radius: 12px;
    overflow: hidden;
  }
  .label--back { left: 30px; background: var(--lime); }
  .label--front { left: 255px; background: var(--green-dark); }
  .label--side { left: 480px; background: var(--lime-bright); }

  /* back label */
  .back-head {
    background: var(--green-dark);
    color: var(--white);
    text-align: center;
    font-size: 11px;
    line-height: 1.3;
    padding: 26px 12px 10px;
  }
  .back-head strong { display: block; font-weight: 800; }
  .facts {
    margin: 0 10px;
    background: var(--white);
    border: 2px solid var(--ink);
    padding: 5px 7px;
    font-size: 8px;
    color: var(--ink);
  }
  .facts h3 { font-size: 15px; font-weight: 800; line-height: 1.1; border-bottom: 1px solid var(--ink); padding-bottom: 2px; }
  .facts .row { display: flex; justify-content: space-between; }
  .facts .row--head { font-weight: 800; border-top: 3px solid var(--ink); border-bottom: 1px solid var(--ink); margin: 3px 0; padding: 1px 0; }
  .facts .formula { text-align: center; font-weight: 800; font-size: 9.5px; margin-top: 8px; line-height: 1.2; }
  .disclaimer {
    margin: 6px 10px 0;
    background: var(--white);
    border: 1px solid var(--ink);
    font-size: 7px;
    font-weight: 700;
    padding: 4px 6px;
    line-height: 1.3;
    color: var(--ink);
  }
  .back-foot {
    display: flex;
    gap: 6px;
    align-items: flex-start;
    margin: 8px 10px 0;
  }
  .badge-plain-circle {
    width: 40px; height: 40px; border-radius: 50%;
    background: var(--white); border: 3px solid var(--green-dark);
    flex: none;
  }
  .badge-plain-square {
    width: 40px; height: 40px; border-radius: 4px;
    background: var(--white); border: 2px solid var(--green-dark);
    flex: none;
  }
  .back-brand {
    border: 1px solid var(--white);
    border-radius: 3px;
    padding: 3px 5px;
    color: var(--white);
    font-size: 7px;
    line-height: 1.3;
  }
  .back-brand b { display: block; font-size: 8px; font-weight: 800; }
  .keep-away {
    margin: 8px 10px 0;
    background: var(--green-dark);
    color: var(--white);
    font-size: 7px;
    font-weight: 800;
    padding: 3px 6px;
    display: inline-block;
  }

  /* front label */
  .front-leaf {
    position: absolute;
    right: -30px; top: -40px;
    width: 140px; height: 130px;
    border-radius: 0 0 0 100px;
    background: linear-gradient(160deg, var(--lime-pale), var(--lime-bright));
  }
  .front-body { position: relative; padding: 70px 0 0 26px; }
  .brand-name {
    font-family: "Nunito", sans-serif;
    font-weight: 800;
    color: var(--white);
    letter-spacing: -0.3px;
  }
  .front-body .brand-name { font-size: 14px; margin-bottom: 38px; }
  .front-hemp { font-family: "Questrial", sans-serif; color: var(--yellow-green); font-size: 26px; line-height: 1; }
  .front-cbd { font-weight: 900; color: var(--yellow-green); font-size: 32px; line-height: 1.05; }
  .front-band {
    margin: 6px 0 0 -26px;
    width: 205px;
    background: var(--lime-bright);
    border-radius: 0 20px 20px 0;
    color: var(--green-deep);
    font-weight: 900;
    font-size: 26px;
    padding: 2px 0 2px 34px;
  }
  .front-herbal { font-family: "Questrial", sans-serif; color: var(--yellow-green); font-size: 17px; margin-top: 8px; }
  .front-flavour {
    font-weight: 800; color: var(--yellow-green); font-size: 14px;
    margin-top: 22px; border-bottom: 2px solid var(--yellow-green);
    width: 150px; padding-bottom: 2px;
  }
  .front-foot { position: absolute; left: 0; right: 0; bottom: 14px; display: flex; align-items: flex-end; gap: 8px; padding-left: 8px; }
  .front-foot .badge-plain-circle { width: 46px; height: 46px; border-color: var(--green-deep); background: var(--yellow-green); }
  .front-foot p { color: var(--white); font-weight: 800; font-size: 12px; line-height: 1.3; }
  .front-foot small { display: block; font-size: 10px; }

  /* side label */
  .side-brand { text-align: center; padding-top: 60px; }
  .side-brand .brand-name { font-size: 14px; }
  .side-panel {
    margin: 36px 16px 0;
    height: 200px;
    border: 10px solid var(--green-mid);
    border-radius: 26px 26px 26px 26px;
    background: var(--lime-bright);
    display: flex; flex-direction: column; justify-content: center;
    padding: 10px 14px;
    text-align: center;
    color: var(--green-deep);
  }
  .side-panel h4 { font-weight: 700; font-size: 14px; margin-bottom: 6px; }
  .side-panel p { font-size: 9px; line-height: 1.45; }
  .side-url { position: absolute; bottom: 22px; left: 0; right: 0; text-align: center; font-family: "Questrial", sans-serif; color: var(--green-dark); font-size: 12px; }

  /* ---------- Carton front ---------- */
  .carton {
    position: absolute;
    left: 730px; top: 110px;
    width: 430px; height: 860px;
    background: var(--lime);
    overflow: hidden;
  }
  .carton-panel {
    position: absolute;
    left: 24px; top: 38px; right: 40px; bottom: 40px;
    background: linear-gradient(180deg, var(--green-deep) 0%, var(--green-mid) 70%, var(--green-dark) 100%);
  }
  .carton-leaf {
    position: absolute;
    right: -40px; top: -10px;
    width: 280px; height: 310px;
    border-radius: 0 0 0 220px;
    background: linear-gradient(150deg, var(--lime-pale), var(--lime-bright) 70%);
  }
  .carton-content { position: absolute; left: 24px; right: 40px; top: 38px; bottom: 40px; }
  .carton .brand-name { position: absolute; top: 290px; left: 80px; font-size: 25px; }
  .carton-hemp { position: absolute; top: 368px; left: 20px; font-family: "Questrial", sans-serif; font-size: 66px; color: var(--yellow-green); line-height: 1; }
  .carton-cbd { position: absolute; top: 432px; left: 20px; font-size: 66px; font-weight: 900; color: var(--yellow-green); line-height: 1; letter-spacing: 0.5px; }
  .carton-band {
    position: absolute; top: 518px; left: 0;
    width: 320px; height: 76px;
    background: var(--lime-bright);
    border-radius: 0 38px 38px 0;
    color: var(--green-deep);
    font-weight: 900; font-size: 56px; line-height: 76px;
    padding-left: 20px;
  }
  .carton-tagline { position: absolute; top: 612px; left: 20px; font-family: "Questrial", sans-serif; color: var(--yellow-green); font-size: 20px; line-height: 1.3; word-spacing: 4px; }
  .carton-herbal { position: absolute; top: 692px; left: 20px; font-family: "Questrial", sans-serif; color: var(--yellow-green); font-size: 30px; }
  .carton-flavour {
    position: absolute; top: 738px; left: 0; width: 240px;
    padding-left: 70px; border-bottom: 3px solid var(--yellow-green);
    font-weight: 800; font-size: 26px; color: var(--yellow-green);
  }
  .carton-flavour-icon { position: absolute; left: 20px; top: 6px; width: 40px; height: 22px; border-radius: 0 14px 0 14px; background: var(--yellow-green); }
  .carton-foot {
    position: absolute; left: 0; right: 0; bottom: 0; height: 100px;
    background: var(--green-deep);
  }
  .carton-foot .badge-plain-circle {
    position: absolute; left: 12px; top: 10px;
    width: 84px; height: 84px;
    background: var(--yellow-green); border: 6px solid var(--green-dark);
  }
  .carton-foot p { position: absolute; left: 115px; top: 12px; color: var(--white); font-weight: 800; font-size: 20px; line-height: 1.8; }
  .carton-foot .volume { display: block; color: var(--yellow-green); font-size: 24px; line-height: 1.3; }
</style>
</head>
<body>

  <!-- Back label -->
  <section class="label label--back">
    <div class="back-head">
      <strong>Ingredients:</strong>
      Pure isolate hemp seed oil, peppermint,
    </div>
    <div class="facts" style="margin-top:10px">
      <h3>Supplement Facts</h3>
      <div>Serving Size : 750 mg</div>
      <div>Serving Per Container : 25 mg/serving</div>
      <div class="row row--head"><span>Amount per serving</span><span>%DV</span></div>
      <div class="row"><span>Calories</span><span>0.0</span></div>
      <div class="row"><span>Calories from Fat</span><span>0.0</span></div>
      <div class="row"><span>Total Fat</span><span>0.0 g</span></div>
      <p class="formula">formulated with organic 99%<br>+ pure Cannabidiol (CBD)</p>
    </div>
    <div class="disclaimer">
      · This product has not been evaluated by the FDA<br>
      · This product is not intended to diagnose, treat, cure or prevent any disease
    </div>
    <div class="back-foot">
      <div class="badge-plain-circle"></div>
      <div class="badge-plain-square"></div>
      <div class="back-brand">
        <b>Steady Meadowcap</b>
        Crafted in small batches from hemp grown on family farms
      </div>
    </div>
    <div class="keep-away">KEEP OUT OF REACH OF CHILDREN</div>
  </section>

  <!-- Front label -->
  <section class="label label--front">
    <div class="front-leaf" role="img" aria-label="Light green leaf with a falling oil drop"></div>
    <div class="front-body">
      <div class="brand-name">Steady Meadowcap</div>
      <div class="front-hemp">HEMP</div>
      <div class="front-cbd">CBD OIL</div>
      <div class="front-band">250+MG</div>
      <div class="front-herbal">HERBAL DROPS</div>
      <div class="front-flavour">Peppermint</div>
    </div>
    <div class="front-foot">
      <div class="badge-plain-circle"></div>
      <p>DIETARY SUPPLEMENT<small>1OZ / 30ML</small></p>
    </div>
  </section>

  <!-- Side label -->
  <section class="label label--side">
    <div class="side-brand"><div class="brand-name">Steady Meadowcap</div></div>
    <div class="side-panel">
      <h4>A pure,</h4>
      <p>full spectrum hemp oil supplement to support medical conditions such as Autism, Anxiety/Depression, PTSD, Autoimmune Disorders, Insomnia, Skin Conditions &amp; more</p>
    </div>
    <div class="side-url">www.steadymeadowcap.example</div>
  </section>

  <!-- Carton front -->
  <section class="carton">
    <div class="carton-panel"></div>
    <div class="carton-leaf" role="img" aria-label="Large light green leaf with an oil drop sweeping over the top corner"></div>
    <div class="carton-content">
      <div class="brand-name">Steady Meadowcap</div>
      <div class="carton-hemp">HEMP</div>
      <div class="carton-cbd">CBD OIL</div>
      <div class="carton-band">250+MG</div>
      <div class="carton-tagline">Calm and Connected<br>Nature’s Perfect Product</div>
      <div class="carton-herbal">HERBAL DROPS</div>
      <div class="carton-flavour">
        <span class="carton-flavour-icon" role="img" aria-label="Peppermint leaves"></span>Peppermint
      </div>
      <div class="carton-foot">
        <div class="badge-plain-circle"></div>
        <p>DIETARY SUPPLEMENT<span class="volume">1OZ / 30ML</span></p>
      </div>
    </div>
  </section>

</body>
</html>
```